Business Card Design Project

I need a cool business card design for the company that will build residential houses.
The card should include:
1) Name: Boris Kalinov
2) Cell: 587.204.XXXX
3) Email: bor.kalinov@qwvend.example
4) Position: General Manager
5) Residential Home Building
6) Company logo that I have uploaded

Industry/Entity Type

Residential

```html
<!DOCTYPE html>
<html lang="en">
<head>
<meta charset="utf-8">
<title>Qwvend Developments – Business Card</title>
<link rel="stylesheet" href="https://fonts.googleapis.com/css2?family=Source+Sans+3:wght@400;600;700&display=swap">
<style>
  :root {
    --page-bg: #e9e7e4;
    --card-white: #ffffff;
    --brand-blue: #2b2f86;
    --brand-blue-deep: #23276f;
    --band-gray: #a9b0b0;
    --accent-green: #2fa84f;
    --text-white: #ffffff;
    --logo-gray: #8a8f94;
  }
  * { box-sizing: border-box; margin: 0; padding: 0; }
  html, body {
    width: 1102px;
    height: 1200px;
    overflow: hidden;
    background: var(--page-bg);
    font-family: "Source Sans 3", Arial, sans-serif;
  }
  .business-card {
    position: absolute;
    left: 61px;
    top: 320px;
    width: 980px;
    height: 560px;
    background: var(--card-white);
    overflow: hidden;
    box-shadow: 0 6px 20px rgba(0,0,0,0.18);
  }
  .card-shapes {
    position: absolute;
    inset: 0;
    width: 100%;
    height: 100%;
  }
  .brand-lockup {
    position: absolute;
    left: 70px;
    top: 120px;
    display: flex;
    align-items: center;
    gap: 18px;
  }
  .brand-dot {
    width: 44px;
    height: 44px;
    border-radius: 50%;
    background: var(--accent-green);
  }
  .brand-name {
    color: var(--brand-blue);
    font-weight: 700;
    font-size: 46px;
    line-height: 1;
    letter-spacing: 1px;
  }
  .contact-block {
    position: absolute;
    right: 50px;
    top: 300px;
    text-align: right;
    color: var(--text-white);
  }
  .person-name {
    font-weight: 600;
    font-size: 40px;
    line-height: 1.05;
    margin-right: 52px;
  }
  .person-role {
    font-weight: 400;
    font-size: 24px;
    margin-right: 52px;
    margin-bottom: 22px;
  }
  .contact-line {
    display: flex;
    justify-content: flex-end;
    align-items: center;
    gap: 18px;
    font-size: 28px;
    line-height: 1;
    height: 40px;
  }
  .contact-icon {
    width: 32px;
    height: 32px;
    border-radius: 4px;
    background: var(--accent-green);
    display: flex;
    align-items: center;
    justify-content: center;
    flex-shrink: 0;
  }
  .contact-icon svg { width: 20px; height: 20px; }
</style>
</head>
<body>
  <section class="business-card" aria-label="Business card front">
    <svg class="card-shapes" viewBox="0 0 980 560" preserveAspectRatio="none" aria-hidden="true">
      <defs>
        <linearGradient id="blueField" x1="0" y1="0" x2="1" y2="1">
          <stop offset="0" stop-color="var(--brand-blue)"/>
          <stop offset="1" stop-color="var(--brand-blue-deep)"/>
        </linearGradient>
      </defs>
      <path class="gray-band" d="M0 366 C 320 330, 640 230, 930 0 L980 0 L980 560 L0 560 Z" fill="var(--band-gray)"/>
      <path class="blue-field" d="M0 384 C 340 350, 680 250, 980 8 L980 560 L0 560 Z" fill="url(#blueField)"/>
    </svg>

    <div class="brand-lockup">
      <span class="brand-dot"></span>
      <span class="brand-name">QWVEND Developments</span>
    </div>

    <div class="contact-block">
      <p class="person-name">Boris Kalinov</p>
      <p class="person-role">General Manager</p>
      <p class="contact-line">587.204.XXXX
        <span class="contact-icon">
          <svg viewBox="0 0 20 20"><rect x="5" y="1.5" width="10" height="17" rx="2" fill="none" stroke="#fff" stroke-width="2"/><circle cx="10" cy="15" r="1.2" fill="#fff"/></svg>
        </span>
      </p>
      <p class="contact-line">bor.kalinov@qwvend.example
        <span class="contact-icon">
          <svg viewBox="0 0 20 20"><rect x="2" y="4.5" width="16" height="11" fill="none" stroke="#fff" stroke-width="2"/><path d="M2 5 L10 11 L18 5" fill="none" stroke="#fff" stroke-width="2"/></svg>
        </span>
      </p>
      <p class="contact-line">www.qwvend.example
        <span class="contact-icon">
          <svg viewBox="0 0 20 20"><circle cx="10" cy="10" r="8" fill="none" stroke="#fff" stroke-width="1.8"/><ellipse cx="10" cy="10" rx="3.5" ry="8" fill="none" stroke="#fff" stroke-width="1.5"/><path d="M2 10 H18" stroke="#fff" stroke-width="1.5"/></svg>
        </span>
      </p>
    </div>
  </section>
</body>
</html>
```